amber tide alliance non profit

I need a simple static website for a non-profit organization that includes blog capacity through Wordpress. The non-profit organization provides education and funding for alternative births and post natal care (doulas and mid-wives) for women. I have the domain name already but not the hosting. I've also set up a gmail account to link to the contact me page.
Updates

Also, would love warm colors.  Background can be white but toolbar and other accents could be peachy warm, tan / mauvish earthy colors.

Thanks.

Target Market(s)

The webstie will be for women who are going through the birthing process or have just given birth. Targeted toward women 16 to 50. The site will include various international outreach programs

Industry/Entity Type

Non Profit

Number of Pages Required

5+ pages

Requirements
Must have
• I want a site that I can control content after it has been designed. So I can add and change copy once it's up. It also must have photo and blog capacity (blog through Wordpress). Toolbar should include (with corresponding pages behind it that I will later include more info that I can update myself) Home, About, Resources / Links, Workshops, Members/Board, Donate Here-sponsors, Forum, International Outreach and somewhere on the homepage: Membership sign-up, Contact.
• The copy attached can be used on the home page.  Then where it explains about the founder, can be in the About section.

• Use warm tones - like peaches or mauvish earthy tan colors for the Toolbars.  (Background can be white.) 
• Use logo (attached) in banner on left and tagline: 
• Non-profit organization providing pre- and postnatal care for women.

• Would like the black and white photo with the mom's hands and baby's feet used as a constant photo and/or in the banner.
Nice to have
• Video capacity for me to add information.  This can be on the blog (through wordpress.)
Should not have
• No stiff, rigid lines.

```html
<!DOCTYPE html>
<html lang="en">
<head>
<meta charset="utf-8">
<title>Amber Tide Alliance – Homepage Concepts</title>
<link href="https://fonts.googleapis.com/css2?family=Open+Sans:ital,wght@0,300;0,400;0,600;0,700;1,700&family=Schoolbell&family=Courgette&display=swap" rel="stylesheet">
<style>
  :root {
    --backdrop: #e9e4dc;
    --bar-red: #b30d12;
    --bar-red-dark: #8e0a0d;
    --pink: #f9c6ef;
    --pink-soft: #f6daf0;
    --paper: #ffffff;
    --brand-blue: #2b3fa6;
    --accent-red: #d0121b;
    --ink: #222222;
    --ink-soft: #555555;
    --tab: #f7efc4;
    --tab-edge: #e3d8a0;
    --rule: #d32a2a;
  }
  * { box-sizing: border-box; margin: 0; padding: 0; }
  html, body { width: 1200px; height: 469px; overflow: hidden; background: var(--backdrop); }
  body { position: relative; font-family: "Open Sans", sans-serif; color: var(--ink); }

  .concept { position: absolute; top: 0; width: 400px; height: 469px; }
  .concept--a { left: 0; }
  .concept--b { left: 400px; }
  .concept--c { left: 800px; }
  .concept-label { position: absolute; left: 13px; top: 4px; font: 700 32px/1 "Open Sans", sans-serif; color: #000; }

  .tagline-bar { position: absolute; left: 63px; top: 22px; width: 304px; height: 38px; background: var(--paper); padding: 6px 6px 0; box-shadow: 0 1px 3px rgba(0,0,0,.25); }
  .tagline-bar__inner { height: 100%; background: linear-gradient(180deg, var(--bar-red), var(--bar-red-dark)); color: #fff; padding: 8px 0 0 8px; font-size: 8.5px; position: relative; white-space: nowrap; }
  .tagline--hand { font-family: "Schoolbell", cursive; font-size: 9px; }
  .tagline--script { font-family: "Courgette", cursive; font-size: 7.6px; }
  .tagline--sans { font-family: "Open Sans", sans-serif; font-weight: 600; font-size: 7.6px; }
  .bar-icons { position: absolute; right: 7px; top: 4px; display: flex; gap: 5px; }

  .page { position: absolute; left: 20px; top: 59px; width: 361px; height: 392px; background: var(--paper); padding: 7px; box-shadow: 0 2px 5px rgba(0,0,0,.3); }
  .page__inner { position: relative; width: 100%; height: 100%; background: linear-gradient(180deg, #fff 0, #fff 68%, var(--pink-soft) 82%, var(--pink-soft) 100%); overflow: hidden; }

  .banner { position: absolute; left: 0; top: 0; width: 100%; height: 133px; background: linear-gradient(135deg, var(--pink), #f3b9e6 60%, var(--pink)); }
  .brand { position: absolute; left: 30px; top: 42px; display: flex; align-items: center; gap: 5px; }
  .brand__dot { width: 14px; height: 14px; border-radius: 50%; background: var(--brand-blue); }
  .brand__name { font: 700 11px/1 "Open Sans", sans-serif; color: var(--brand-blue); }

  .login { position: absolute; left: 30px; top: 96px; }
  .login__field { width: 72px; height: 9px; background: #fff; border: 1px solid #aaa; font-size: 4.5px; color: #666; padding: 1px 2px; margin-bottom: 4px; }
  .login__button { position: absolute; left: 78px; top: 6px; width: 34px; height: 9px; background: #fff; font: 6px/9px "Schoolbell", cursive; text-align: center; transform: rotate(-3deg); box-shadow: 0 1px 1px rgba(0,0,0,.2); }
  .login__forgot { font-size: 4px; margin-top: 2px; }
  .login__forgot span { text-decoration: underline; color: #1a1a80; }

  .hero-photo { position: absolute; left: 192px; top: 0; width: 120px; height: 140px; transform: rotate(-8deg); background: radial-gradient(ellipse at 50% 45%, #cfcfcf 0, #7d7d7d 25%, #111 55%, #000 100%); box-shadow: 1px 2px 4px rgba(0,0,0,.4); }

  .nav { position: absolute; left: 5px; top: 144px; list-style: none; }
  .nav__item { width: 68px; height: 12px; margin-bottom: 6.5px; background: var(--tab); border-bottom: 1px solid var(--tab-edge); font-size: 5.6px; letter-spacing: .6px; text-align: center; line-height: 12px; box-shadow: 1px 1px 2px rgba(0,0,0,.15); }
  .nav__item:nth-child(2n) { transform: rotate(1deg); }
  .nav__divider { position: absolute; left: 85px; top: 144px; height: 111px; border-left: 1px dotted var(--rule); }

  .welcome { position: absolute; left: 99px; top: 149px; width: 178px; }
  .welcome__title { font: 300 16px/1 "Open Sans", sans-serif; color: #555; border-bottom: 1px solid #bbb; padding-bottom: 1px; }
  .welcome__lead { color: var(--accent-red); font-size: 5.2px; line-height: 9.3px; margin-top: 5px; }
  .welcome__body { font-size: 4.4px; line-height: 9.3px; margin-top: 4px; }
  .side-photo { position: absolute; left: 290px; top: 148px; width: 48px; height: 64px; transform: rotate(15deg); background: linear-gradient(160deg, #e2c28a, #8a5a32 55%, #2a1a12); border: 2px solid #f3e7c6; }

  .cta-rule { position: absolute; left: 16px; top: 270px; width: 316px; border-top: 1px dotted var(--rule); }
  .cta { position: absolute; top: 274px; display: flex; align-items: baseline; gap: 3px; font-size: 9.2px; white-space: nowrap; }
  .cta small { font-size: 5px; }
  .cta--join { left: 16px; }
  .cta--donate { left: 218px; }

  .features { position: absolute; left: 10px; top: 295px; width: 330px; display: flex; justify-content: space-between; }
  .feature { width: 98px; text-align: center; }
  .feature__photo { width: 90px; height: 50px; margin: 0 auto; border: 2px solid #fff; box-shadow: 0 0 2px rgba(0,0,0,.2); }
  .feature__photo--outreach { background: linear-gradient(180deg, #4b88d6, #a9c9ee 70%, #e0734a); }
  .feature__photo--volunteers { background: linear-gradient(135deg, #a4756a, #e2b8a6 60%, #c98f80); }
  .feature__photo--events { background: linear-gradient(90deg, #e8c49b, #f1dcc5 45%, #8a8a7c); }
  .feature__title { font-size: 6.6px; margin-top: 4px; letter-spacing: .2px; }
  .feature__text { font-size: 3.8px; line-height: 5px; color: var(--ink); }
  .features__divider { position: absolute; top: 293px; height: 75px; border-left: 1px dotted var(--rule); }
</style>
</head>
<body>

<!-- Concept A -->
<section class="concept concept--a">
  <div class="concept-label">A</div>
  <div class="tagline-bar"><div class="tagline-bar__inner tagline--hand">Non-profit organization providing pre &amp; postnatal care for women
    <span class="bar-icons"><svg width="6" height="5" viewBox="0 0 6 5"><rect x=".5" y=".5" width="5" height="4" fill="none" stroke="#f3b" stroke-width=".6"/><path d="M.5 .5 3 2.6 5.5 .5" fill="none" stroke="#f3b" stroke-width=".6"/></svg><svg width="6" height="5" viewBox="0 0 6 5"><path d="M.5 2.5 3 .4 5.5 2.5V4.6H.5Z" fill="none" stroke="#f3b" stroke-width=".6"/></svg></span></div></div>
  <div class="page"><div class="page__inner">
    <div class="banner">
      <div class="brand"><span class="brand__dot"></span><span class="brand__name">Amber Tide Alliance</span></div>
      <div class="login"><div class="login__field">Username</div><div class="login__field">•••••••••••</div><div class="login__button">LOGIN</div><div class="login__forgot">Forgot username? <span>Click here</span></div></div>
    </div>
    <div class="hero-photo" role="img" aria-label="Black and white photo of a mother's hands shaping a heart around a baby's feet"></div>
    <ul class="nav"><li class="nav__item">ABOUT</li><li class="nav__item">RESOURCES</li><li class="nav__item">WORKSHOPS</li><li class="nav__item">FORUM</li><li class="nav__item">BOARD</li></ul>
    <div class="nav__divider"></div>
    <div class="welcome"><h1 class="welcome__title">welcome</h1>
      <p class="welcome__lead">Help us help our sisters and daughters to take back control over how we bring the next generation to life</p>
      <p class="welcome__body">Phasellus ut placerat risus. Fusce a erat massa. Curabitur sapien massa, tempus euismod aliquam vitae, bibendum ac dui. Class aptent taciti sociosqu ad litora torquent per conubia nostra, per inceptos himenaeos. Aliquam erat volutpat. Pellentesque elementum leo in purus eleifend at iaculis quam commodo. Nulla ante lorem, convallis vel auctor ut, fermentum nec ante. Donec viverra consequat lacus, non sodales nibh suscipit vel. Quisque sagittis velit nec mi placerat suscipit. Nam tincidunt pharetra congue.</p></div>
    <div class="side-photo" role="img" aria-label="Photo of a smiling expectant mother"></div>
    <div class="cta-rule"></div>
    <div class="cta cta--join"><svg width="10" height="8" viewBox="0 0 10 8"><path d="M0 0 10 4 0 8 3 4Z" fill="var(--accent-red)"/></svg>Join here,<small>free membership and newsletter</small></div>
    <div class="cta cta--donate"><svg width="10" height="8" viewBox="0 0 10 8"><path d="M0 0 10 4 0 8 3 4Z" fill="var(--accent-red)"/></svg>Donate here,<small>for a good cause</small></div>
    <div class="features__divider" style="left:112px"></div><div class="features__divider" style="left:228px"></div>
    <div class="features">
      <div class="feature"><div class="feature__photo feature__photo--outreach" role="img" aria-label="Photo of a mother and child playing outdoors under a blue sky"></div><h2 class="feature__title">INTERNATIONAL OUTREACH</h2><p class="feature__text">Adopt/create a healthcare facility overseas</p></div>
      <div class="feature"><div class="feature__photo feature__photo--volunteers" role="img" aria-label="Photo of a newborn's hand held by an adult"></div><h2 class="feature__title">VOLUNTEERS</h2><p class="feature__text">Doulas, baby sitters, insurance, legal experts, musicians' soothing music, meditations, yogis</p></div>
      <div class="feature"><div class="feature__photo feature__photo--events" role="img" aria-label="Photo of a toddler beside a pregnant belly"></div><h2 class="feature__title">EVENTS &amp; NEWS</h2><p class="feature__text">Latest updates &amp; information from around the world</p></div>
    </div>
  </div></div>
</section>

<!-- Concept B -->
<section class="concept concept--b">
  <div class="concept-label">B</div>
  <div class="tagline-bar"><div class="tagline-bar__inner tagline--script">Non-profit organization providing pre &amp; postnatal care for women
    <span class="bar-icons"><svg width="6" height="5" viewBox="0 0 6 5"><rect x=".5" y=".5" width="5" height="4" fill="none" stroke="#f3b" stroke-width=".6"/><path d="M.5 .5 3 2.6 5.5 .5" fill="none" stroke="#f3b" stroke-width=".6"/></svg><svg width="6" height="5" viewBox="0 0 6 5"><path d="M.5 2.5 3 .4 5.5 2.5V4.6H.5Z" fill="none" stroke="#f3b" stroke-width=".6"/></svg></span></div></div>
  <div class="page"><div class="page__inner">
    <div class="banner">
      <div class="brand"><span class="brand__dot"></span><span class="brand__name">Amber Tide Alliance</span></div>
      <div class="login"><div class="login__field">Username</div><div class="login__field">•••••••••••</div><div class="login__button">LOGIN</div><div class="login__forgot">Forgot username? <span>Click here</span></div></div>
    </div>
    <div class="hero-photo" role="img" aria-label="Black and white photo of a mother's hands shaping a heart around a baby's feet"></div>
    <ul class="nav"><li class="nav__item">ABOUT</li><li class="nav__item">RESOURCES</li><li class="nav__item">WORKSHOPS</li><li class="nav__item">FORUM</li><li class="nav__item">BOARD</li></ul>
    <div class="nav__divider"></div>
    <div class="welcome"><h1 class="welcome__title">welcome</h1>
      <p class="welcome__lead">Help us help our sisters and daughters to take back control over how we bring the next generation to life</p>
      <p class="welcome__body">Phasellus ut placerat risus. Fusce a erat massa. Curabitur sapien massa, tempus euismod aliquam vitae, bibendum ac dui. Class aptent taciti sociosqu ad litora torquent per conubia nostra, per inceptos himenaeos. Aliquam erat volutpat. Pellentesque elementum leo in purus eleifend at iaculis quam commodo. Nulla ante lorem, convallis vel auctor ut, fermentum nec ante. Donec viverra consequat lacus, non sodales nibh suscipit vel. Quisque sagittis velit nec mi placerat suscipit. Nam tincidunt pharetra congue.</p></div>
    <div class="side-photo" role="img" aria-label="Photo of a smiling expectant mother"></div>
    <div class="cta-rule"></div>
    <div class="cta cta--join"><svg width="10" height="8" viewBox="0 0 10 8"><path d="M0 0 10 4 0 8 3 4Z" fill="var(--accent-red)"/></svg>Join here,<small>free membership and newsletter</small></div>
    <div class="cta cta--donate"><svg width="10" height="8" viewBox="0 0 10 8"><path d="M0 0 10 4 0 8 3 4Z" fill="var(--accent-red)"/></svg>Donate here,<small>for a good cause</small></div>
    <div class="features__divider" style="left:112px"></div><div class="features__divider" style="left:228px"></div>
    <div class="features">
      <div class="feature"><div class="feature__photo feature__photo--outreach" role="img" aria-label="Photo of a mother and child playing outdoors under a blue sky"></div><h2 class="feature__title">INTERNATIONAL OUTREACH</h2><p class="feature__text">Adopt/create a healthcare facility overseas</p></div>
      <div class="feature"><div class="feature__photo feature__photo--volunteers" role="img" aria-label="Photo of a newborn's hand held by an adult"></div><h2 class="feature__title">VOLUNTEERS</h2><p class="feature__text">Doulas, baby sitters, insurance, legal experts, musicians' soothing music, meditations, yogis</p></div>
      <div class="feature"><div class="feature__photo feature__photo--events" role="img" aria-label="Photo of a toddler beside a pregnant belly"></div><h2 class="feature__title">EVENTS &amp; NEWS</h2><p class="feature__text">Latest updates &amp; information from around the world</p></div>
    </div>
  </div></div>
</section>

<!-- Concept C -->
<section class="concept concept--c">
  <div class="concept-label">C</div>
  <div class="tagline-bar"><div class="tagline-bar__inner tagline--sans">Non-profit organization providing pre &amp; postnatal care for women
    <span class="bar-icons"><svg width="6" height="5" viewBox="0 0 6 5"><rect x=".5" y=".5" width="5" height="4" fill="none" stroke="#f3b" stroke-width=".6"/><path d="M.5 .5 3 2.6 5.5 .5" fill="none" stroke="#f3b" stroke-width=".6"/></svg><svg width="6" height="5" viewBox="0 0 6 5"><path d="M.5 2.5 3 .4 5.5 2.5V4.6H.5Z" fill="none" stroke="#f3b" stroke-width=".6"/></svg></span></div></div>
  <div class="page"><div class="page__inner">
    <div class="banner">
      <div class="brand"><span class="brand__dot"></span><span class="brand__name">Amber Tide Alliance</span></div>
      <div class="login"><div class="login__field">Username</div><div class="login__field">•••••••••••</div><div class="login__button">LOGIN</div><div class="login__forgot">Forgot username? <span>Click here</span></div></div>
    </div>
    <div class="hero-photo" role="img" aria-label="Black and white photo of a mother's hands shaping a heart around a baby's feet"></div>
    <ul class="nav"><li class="nav__item">ABOUT</li><li class="nav__item">RESOURCES</li><li class="nav__item">WORKSHOPS</li><li class="nav__item">FORUM</li><li class="nav__item">BOARD</li></ul>
    <div class="nav__divider"></div>
    <div class="welcome"><h1 class="welcome__title">welcome</h1>
      <p class="welcome__lead">Help us help our sisters and daughters to take back control over how we bring the next generation to life</p>
      <p class="welcome__body">Phasellus ut placerat risus. Fusce a erat massa. Curabitur sapien massa, tempus euismod aliquam vitae, bibendum ac dui. Class aptent taciti sociosqu ad litora torquent per conubia nostra, per inceptos himenaeos. Aliquam erat volutpat. Pellentesque elementum leo in purus eleifend at iaculis quam commodo. Nulla ante lorem, convallis vel auctor ut, fermentum nec ante. Donec viverra consequat lacus, non sodales nibh suscipit vel. Quisque sagittis velit nec mi placerat suscipit. Nam tincidunt pharetra congue.</p></div>
    <div class="side-photo" role="img" aria-label="Photo of a smiling expectant mother"></div>
    <div class="cta-rule"></div>
    <div class="cta cta--join"><svg width="10" height="8" viewBox="0 0 10 8"><path d="M0 0 10 4 0 8 3 4Z" fill="var(--accent-red)"/></svg>Join here,<small>free membership and newsletter</small></div>
    <div class="cta cta--donate"><svg width="10" height="8" viewBox="0 0 10 8"><path d="M0 0 10 4 0 8 3 4Z" fill="var(--accent-red)"/></svg>Donate here,<small>for a good cause</small></div>
    <div class="features__divider" style="left:112px"></div><div class="features__divider" style="left:228px"></div>
    <div class="features">
      <div class="feature"><div class="feature__photo feature__photo--outreach" role="img" aria-label="Photo of a mother and child playing outdoors under a blue sky"></div><h2 class="feature__title">INTERNATIONAL OUTREACH</h2><p class="feature__text">Adopt/create a healthcare facility overseas</p></div>
      <div class="feature"><div class="feature__photo feature__photo--volunteers" role="img" aria-label="Photo of a newborn's hand held by an adult"></div><h2 class="feature__title">VOLUNTEERS</h2><p class="feature__text">Doulas, baby sitters, insurance, legal experts, musicians' soothing music, meditations, yogis</p></div>
      <div class="feature"><div class="feature__photo feature__photo--events" role="img" aria-label="Photo of a toddler beside a pregnant belly"></div><h2 class="feature__title">EVENTS &amp; NEWS</h2><p class="feature__text">Latest updates &amp; information from around the world</p></div>
    </div>
  </div></div>
</section>

</body>
</html>
```